BrivaTrek Freight Services Business cards

Would like a very unique design catchy but professional for business cards. Please use log provided.Marlon WellsCeo and Founder TransCon Logistix Solutions1-888-913-3225mwells@tlsolutionsus.comwww.bfservicesco.com

```html
<!DOCTYPE html>
<html lang="en">
<head>
<meta charset="utf-8">
<title>BrivaTrek Freight Services – Business Cards</title>
<link rel="stylesheet" href="https://fonts.googleapis.com/css2?family=Open+Sans:wght@400;600;700&display=swap">
<style>
  :root {
    --backdrop: #e9e7e3;
    --navy: #0b2742;
    --blue: #1576c0;
    --brand-blue: #1a6fb7;
    --red: #e42027;
    --white: #ffffff;
    --ink: #2b2b2b;
    --rule: #9a9a9a;
  }
  * { margin: 0; padding: 0; box-sizing: border-box; }
  html, body {
    width: 1200px; height: 960px; overflow: hidden;
    background: var(--backdrop);
    font-family: "Open Sans", Arial, sans-serif;
  }
  .canvas { position: relative; width: 1200px; height: 960px; }

  .card {
    position: absolute; overflow: hidden; border-radius: 36px;
    box-shadow: 0 6px 18px rgba(0,0,0,0.25);
  }

  /* Back of card */
  .card-back {
    left: 236px; top: 46px; width: 722px; height: 406px;
    background: var(--navy); color: var(--white);
  }
  .card-back .brand-name {
    position: absolute; left: 0; right: 0; top: 118px;
    text-align: center; font-weight: 700; font-size: 58px; line-height: 1.12;
    letter-spacing: 1px;
  }
  .card-back .website {
    position: absolute; left: 0; right: 0; top: 300px;
    text-align: center; font-size: 19px; letter-spacing: 3px;
  }
  .card-back .website strong { font-weight: 700; }

  /* Front of card */
  .card-front {
    left: 244px; top: 508px; width: 706px; height: 406px;
    background: var(--white);
  }
  .card-front .wave { position: absolute; inset: 0; width: 706px; height: 406px; }
  .card-front .person {
    position: absolute; right: 30px; top: 30px; text-align: right; color: var(--white);
  }
  .person .name { font-size: 21px; font-weight: 700; letter-spacing: 0.3px; }
  .person .role { font-size: 17px; font-weight: 400; margin-top: 4px; }

  .card-front .brand-name {
    position: absolute; left: 30px; top: 100px; width: 360px;
    text-align: center; color: var(--brand-blue);
    font-weight: 700; font-size: 30px; line-height: 1.2;
  }

  .contacts {
    position: absolute; left: 30px; top: 286px; list-style: none;
    font-size: 16px; color: var(--ink);
  }
  .contacts li { display: flex; align-items: center; height: 30px; }
  .contacts svg { width: 14px; height: 14px; margin-right: 12px; flex: none; }

  .divider {
    position: absolute; left: 295px; top: 318px; width: 1px; height: 62px;
    background: var(--rule);
  }
  .address {
    position: absolute; left: 314px; top: 318px;
    font-size: 16px; line-height: 27px; color: var(--ink); font-style: normal;
  }
</style>
</head>
<body>
<div class="canvas">

  <section class="card card-back">
    <div class="brand-name">BrivaTrek<br>Freight Services</div>
    <div class="website">www.<strong>bfservicesco</strong>.com</div>
  </section>

  <section class="card card-front">
    <svg class="wave" viewBox="0 0 706 406" aria-hidden="true">
      <path fill="var(--red)" d="M0,0 H706 V242 C560,142 330,16 160,24 C90,28 38,50 0,80 Z"/>
      <path fill="var(--white)" d="M0,0 H706 V214 C560,124 330,8 160,18 C90,22 38,44 0,74 Z"/>
      <path fill="var(--blue)" d="M0,0 H706 V202 C560,116 330,4 160,14 C90,18 38,40 0,70 Z"/>
      <path fill="var(--red)" d="M0,70 C38,40 90,18 160,14 C180,13 200,13 222,14 C200,15 180,17 160,19 C90,24 38,46 0,76 Z"/>
    </svg>

    <div class="person">
      <div class="name">DUSTIN HARROW</div>
      <div class="role">CEO AND FOUNDER</div>
    </div>

    <div class="brand-name">BrivaTrek<br>Freight Services</div>

    <ul class="contacts">
      <li>
        <svg viewBox="0 0 14 14"><circle cx="7" cy="7" r="6" fill="none" stroke="var(--blue)" stroke-width="1.4"/><path d="M5 3.8 L6.2 5.6 L5.4 6.4 C6 7.6 6.6 8.3 7.6 8.8 L8.4 8 L10.2 9.2 L9.4 10.4 C6.6 10.2 3.8 7.4 3.6 4.6 Z" fill="var(--blue)"/></svg>
        1-888-472-6081
      </li>
      <li>
        <svg viewBox="0 0 14 14"><rect x="1" y="3" width="12" height="8" rx="1" fill="var(--blue)"/><path d="M1.5 3.6 L7 7.6 L12.5 3.6" fill="none" stroke="var(--white)" stroke-width="1.2"/></svg>
        dharrow@bfservicesco.com
      </li>
      <li>
        <svg viewBox="0 0 14 14"><g fill="none" stroke="var(--blue)" stroke-width="1.2"><circle cx="7" cy="7" r="6"/><ellipse cx="7" cy="7" rx="2.6" ry="6"/><path d="M1 7 H13 M2 4 H12 M2 10 H12"/></g></svg>
        www.bfservicesco.com
      </li>
    </ul>

    <div class="divider"></div>
    <address class="address">742 Calloway Ridge Rd<br>Marietta, GA 30062</address>
  </section>

</div>
</body>
</html>
```